Harbinger Noble Alloys Works Business Cards

We are wanting to have a new business card designed for our company as we go to a convention. We want to balance business/Modern with elegance and beauty. Our company sells highend jewelry pieces. We want to utilize the colors of Black and Gold and have gold foiled fonts to be physically printed on the business cards.
We also would like to have space to write notes on the back side of the business card. When we meet people at jewelry conventions we would like to write notes if possible.
Here are websites and designs that we like the look and feel of these companies and you can use these as design ideas.
https://www.lorvanne.com
https://www.bellquist.com/en-us/home
Here is our company website link
www.harbingernaw.com
I also up loaded two versions of our logo.
- Update 4.26.22
I have uploaded photos of a business card we like. this card has raised embossed letters that you can feel. the raise letters are like a plastic but we don't need to use that...I uploaded to show you that we like the experience of the client feeling the characters of the logo. we also would like to have the material as a satin or some material very soft.
- Maybe we can get designs with beautiful gold foiling and raised characters and logos. we like simplicity...not busy but an elegant design. We need to write notes and would like a section where we can write notes. but we want an elegant style and the client has an experience with the feel of the card when they touch the card.
Colors
- Main colors Black & Gold
- white or light colors for small notes section.
Specialty ideals and things we would like to see based on your design styles.
- raised fonts
- raised logos
- gold foiling
- satin/soft finish on the card material.
we are wanting to design a business card that looks elegant and clean. When the client is handed the business card we want them to physically experience the business card as well by touching the raised logos or fonts and the base material is soft satin. I hope this helps with further designs.
thank you all
We uploaded a new contact layout that we have designed in our office. we would like to see how this would look on your designs.
thank you
I just finished uploading the Contact Layout. the colors are just examples. please use this layout as an idea and use colors based on the feed back we have given each of you personally.
Contact Information for Business Card
we need an area to write notes, we would like to have our logos or the diamond of our logo or the business card to have embossed sections to the business card so when the customer touches the card they can feel the logo. we would also like sections of our business card to have gold foiling. we would also like to use a satin soft paper with our card. when the client touches the card its super soft and high quality
Requirements
Must have
- we would like to have our logos or the diamond of our logo or the business card to have embossed sections to the business card so when the customer touches the card they can feel the logo. we would also like sections of our business card to have gold foiling. we would also like to use a satin soft paper with our card. when the client touches the card its super soft and high quality
Nice to have
- we would like to have our logos or the diamond of our logo or the business card to have embossed sections to the business card so when the customer touches the card they can feel the logo. we would also like sections of our business card to have gold foiling.

```html
<!DOCTYPE html>
<html lang="en">
<head>
<meta charset="utf-8">
<title>Harbinger Noble Alloys Works – Business Cards</title>
<link rel="stylesheet" href="https://fonts.googleapis.com/css2?family=Cinzel:wght@400&family=Montserrat:wght@400;600&display=swap">
<style>
  :root {
    --ink: #000000;
    --gold: #d6a62c;
    --gold-line: #6b5418;
    --white: #ffffff;
    --stage-top: #d9d9d9;
    --stage-bottom: #ffffff;
    --deco: rgba(255,255,255,0.045);
  }
  * { margin: 0; padding: 0; box-sizing: border-box; }
  html, body { width: 1200px; height: 2542px; overflow: hidden; }
  body { position: relative; background: var(--stage-bottom); font-family: "Montserrat", Arial, sans-serif; }
  .stage-band { position: absolute; left: 0; top: 0; width: 1200px; height: 1263px; background: var(--stage-top); }

  .card {
    position: absolute;
    width: calc(var(--s) * 882px);
    height: calc(var(--s) * 505px);
    background: var(--ink);
    overflow: hidden;
    box-shadow: 0 3px 6px rgba(0,0,0,0.35);
  }
  .card-1 { --s: 1; left: 166px; top: 78px; }
  .card-2 { --s: 1; left: 166px; top: 630px; }
  .card-3 { --s: 1.04; left: 149px; top: 1337px; }
  .card-4 { --s: 1.04; left: 149px; top: 1911px; }

  .decoration {
    position: absolute;
    right: 0;
    top: calc(var(--s) * 75px);
    width: calc(var(--s) * 520px);
    height: calc(var(--s) * 430px);
    background: radial-gradient(ellipse at 70% 40%, var(--deco), rgba(255,255,255,0) 70%);
  }

  .brand {
    position: absolute; left: 0; right: 0;
    text-align: center;
    font-family: "Cinzel", "Times New Roman", serif;
    font-weight: 400;
    color: var(--white);
    line-height: 1;
  }
  .brand-name { display: block; }
  .brand-tagline { display: block; }

  .front .brand { top: calc(var(--s) * 198px); }
  .front .brand-name { font-size: calc(var(--s) * 34px); }
  .front .brand-tagline { font-size: calc(var(--s) * 28px); margin-top: calc(var(--s) * 12px); }

  .back .brand { top: calc(var(--s) * 111px); }
  .back .brand-name { font-size: calc(var(--s) * 26px); }
  .back .brand-tagline { font-size: calc(var(--s) * 21px); margin-top: calc(var(--s) * 8px); }

  .website {
    position: absolute; left: 0; right: 0;
    top: calc(var(--s) * 386px);
    text-align: center;
    color: var(--gold);
    font-size: calc(var(--s) * 29px);
    letter-spacing: calc(var(--s) * 4.5px);
  }

  .contact-list { position: absolute; left: calc(var(--s) * 64px); top: 0; list-style: none; }
  .contact-item { position: absolute; left: 0; display: flex; align-items: center; white-space: nowrap; color: var(--gold); letter-spacing: calc(var(--s) * 1.4px); }
  .contact-item svg { width: calc(var(--s) * 28px); height: calc(var(--s) * 28px); flex: none; margin-right: calc(var(--s) * 24px); }
  .contact-phone { top: calc(var(--s) * 256px); font-size: calc(var(--s) * 23px); font-weight: 600; letter-spacing: calc(var(--s) * 0.5px); }
  .contact-email { top: calc(var(--s) * 304px); font-size: calc(var(--s) * 16px); }
  .contact-address { top: calc(var(--s) * 350px); font-size: calc(var(--s) * 16px); line-height: 1.35; }
  .contact-web { top: calc(var(--s) * 414px); font-size: calc(var(--s) * 16px); }

  .notes { position: absolute; left: calc(var(--s) * 474px); top: calc(var(--s) * 258px); width: calc(var(--s) * 338px); }
  .notes-title { text-align: center; color: var(--gold); font-size: calc(var(--s) * 24px); letter-spacing: calc(var(--s) * 1px); font-weight: 400; line-height: 1; }
  .note-line { position: absolute; left: 0; width: 100%; height: 1px; background: var(--gold-line); }
  .note-line:nth-of-type(1) { top: calc(var(--s) * 50px); }
  .note-line:nth-of-type(2) { top: calc(var(--s) * 85px); }
  .note-line:nth-of-type(3) { top: calc(var(--s) * 126px); }
  .note-line:nth-of-type(4) { top: calc(var(--s) * 165px); }
</style>
</head>
<body>
<div class="stage-band"></div>

<!-- Card set one -->
<section class="card front card-1">
  <div class="decoration" role="img" aria-label="Faint large gem and scroll decoration"></div>
  <h1 class="brand"><span class="brand-name">Harbinger Noble Alloys Works</span><span class="brand-tagline">– Coins, Jewelry &amp; Diamonds –</span></h1>
  <p class="website">www.harbingernaw.com</p>
</section>

<section class="card back card-2">
  <div class="decoration" role="img" aria-label="Faint large gem and scroll decoration"></div>
  <h2 class="brand"><span class="brand-name">Harbinger Noble Alloys Works</span><span class="brand-tagline">– Coins, Jewelry &amp; Diamonds –</span></h2>
  <ul class="contact-list">
    <li class="contact-item contact-phone"><svg viewBox="0 0 24 24" fill="none" stroke="#d6a62c" stroke-width="2" stroke-linecap="round" stroke-linejoin="round"><path d="M5 3h4l2 5-3 2a12 12 0 0 0 6 6l2-3 5 2v4a2 2 0 0 1-2 2A18 18 0 0 1 3 5a2 2 0 0 1 2-2z"/></svg>(503) 555-0142</li>
    <li class="contact-item contact-email"><svg viewBox="0 0 24 24" fill="none" stroke="#d6a62c" stroke-width="2" stroke-linejoin="round"><rect x="2" y="5" width="20" height="14"/><path d="M2 5l10 8 10-8"/></svg>info@harbingernaw.com</li>
    <li class="contact-item contact-address"><svg viewBox="0 0 24 24" fill="none" stroke="#d6a62c" stroke-width="2" stroke-linejoin="round"><path d="M12 21s-6-6.5-6-11a6 6 0 0 1 12 0c0 4.5-6 11-6 11z"/><circle cx="12" cy="10" r="2.2"/></svg><span>4127 Verbena Ave NE<br>Salem, Oregon USA 97301</span></li>
    <li class="contact-item contact-web"><svg viewBox="0 0 24 24" fill="none" stroke="#d6a62c" stroke-width="2"><circle cx="12" cy="12" r="9"/><path d="M3 12h18M12 3c3 3 3 15 0 18M12 3c-3 3-3 15 0 18"/></svg>harbingernaw.com</li>
  </ul>
  <div class="notes">
    <p class="notes-title">NOTE</p>
    <span class="note-line"></span><span class="note-line"></span><span class="note-line"></span><span class="note-line"></span>
  </div>
</section>

<!-- Card set two -->
<section class="card front card-3">
  <div class="decoration" role="img" aria-label="Faint large gem and scroll decoration"></div>
  <h2 class="brand"><span class="brand-name">Harbinger Noble Alloys Works</span><span class="brand-tagline">– Coins, Jewelry &amp; Diamonds –</span></h2>
  <p class="website">www.harbingernaw.com</p>
</section>

<section class="card back card-4">
  <div class="decoration" role="img" aria-label="Faint large gem and scroll decoration"></div>
  <h2 class="brand"><span class="brand-name">Harbinger Noble Alloys Works</span><span class="brand-tagline">– Coins, Jewelry &amp; Diamonds –</span></h2>
  <ul class="contact-list">
    <li class="contact-item contact-phone"><svg viewBox="0 0 24 24" fill="none" stroke="#d6a62c" stroke-width="2" stroke-linecap="round" stroke-linejoin="round"><path d="M5 3h4l2 5-3 2a12 12 0 0 0 6 6l2-3 5 2v4a2 2 0 0 1-2 2A18 18 0 0 1 3 5a2 2 0 0 1 2-2z"/></svg>(503) 555-0142</li>
    <li class="contact-item contact-email"><svg viewBox="0 0 24 24" fill="none" stroke="#d6a62c" stroke-width="2" stroke-linejoin="round"><rect x="2" y="5" width="20" height="14"/><path d="M2 5l10 8 10-8"/></svg>info@harbingernaw.com</li>
    <li class="contact-item contact-address"><svg viewBox="0 0 24 24" fill="none" stroke="#d6a62c" stroke-width="2" stroke-linejoin="round"><path d="M12 21s-6-6.5-6-11a6 6 0 0 1 12 0c0 4.5-6 11-6 11z"/><circle cx="12" cy="10" r="2.2"/></svg><span>4127 Verbena Ave NE<br>Salem, Oregon USA 97301</span></li>
    <li class="contact-item contact-web"><svg viewBox="0 0 24 24" fill="none" stroke="#d6a62c" stroke-width="2"><circle cx="12" cy="12" r="9"/><path d="M3 12h18M12 3c3 3 3 15 0 18M12 3c-3 3-3 15 0 18"/></svg>harbingernaw.com</li>
  </ul>
  <div class="notes">
    <p class="notes-title">NOTE</p>
    <span class="note-line"></span><span class="note-line"></span><span class="note-line"></span><span class="note-line"></span>
  </div>
</section>
</body>
</html>
```